Create a web design for a vehicle codes lookup website

Create a bright and fun web design to replace our current boring one!

-Make a new design for this page that shows vehicle codes information: http://plinkor.net/vin/mara-dulek.4182.html
-Click "Random VIN" to see more examples.
-The page shows the vehicle information (see above example) is the most important one to add a redesign to. Bonus points if you create a redesign for the main page as well: plinkor.net.

Number of Pages Required

2 page

Requirements
Must have
• Be fun and have bright colors!
Should not have
• Do not add pictures of specific people or vehicles unless they can be used on every page. The example page has a Brevik Solano, but do not add a picture of the Brevik Solano because other pages have different vehicles.

```html
<!DOCTYPE html>
<html lang="en">
<head>
<meta charset="utf-8">
<title>plinkor.net – Vehicle Codes</title>
<link href="https://fonts.googleapis.com/css2?family=Arimo:ital,wght@0,400;0,700;1,700&display=swap" rel="stylesheet">
<style>
:root{
  --navy:#0c3a63;
  --navy-deep:#072a4b;
  --blue:#1a5a8f;
  --green:#4cae2a;
  --green-dark:#2f8a17;
  --white:#ffffff;
  --grey-panel:rgba(120,120,120,.72);
  --text-dark:#333;
  --muted:#666;
}
*{box-sizing:border-box;margin:0;padding:0}
html,body{width:681px;height:1200px;overflow:hidden}
body{font-family:"Arimo",Arial,sans-serif;background:var(--navy);color:var(--text-dark);font-size:10px}
.page{position:relative;width:681px;height:1200px;background:linear-gradient(var(--navy),var(--navy-deep))}
.header{position:absolute;left:0;top:0;width:681px;height:92px;padding:0 22px}
.logo{position:absolute;left:22px;top:34px;color:var(--white);font-weight:700;font-size:22px;letter-spacing:1px}
.header-actions{position:absolute;right:22px;top:44px;display:flex;gap:8px;align-items:center}
.btn{display:inline-block;background:var(--green);color:var(--white);font-size:9px;border-radius:3px;padding:4px 9px;text-decoration:none}
.btn-dark{background:var(--navy);border:1px solid #4c7cab}
.search-input{width:140px;height:22px;background:var(--white);border-radius:3px;font-size:9px;color:#999;padding:5px 7px}
.search-btn{width:22px;height:22px;border-radius:3px;background:var(--green);display:flex;align-items:center;justify-content:center}
.nav{position:absolute;left:22px;top:92px;width:637px;height:14px;background:var(--green);display:flex;justify-content:flex-end;gap:0;padding-right:10px}
.nav a{color:var(--white);font-size:7px;padding:3px 8px;text-decoration:none;border-left:1px solid rgba(255,255,255,.5)}
.nav a:first-child{border-left:0}
.hero{position:absolute;left:22px;top:106px;width:637px;height:280px;background:var(--white)}
.hero-photo{position:absolute;left:12px;top:20px;width:360px;height:200px;border-radius:40% 50% 20% 20%/50% 50% 20% 20%;background:radial-gradient(ellipse at 50% 55%,#f2f2f2,#bfc3c6 60%,#fff 72%)}
.hero-copy{position:absolute;right:18px;top:30px;width:260px;text-align:right}
.hero-copy h1{color:var(--blue);font-weight:400;font-size:24px;line-height:1.15}
.hero-copy p{color:var(--blue);font-size:10px;margin-top:8px;line-height:1.35}
.hero-copy .actions{margin-top:12px;display:flex;gap:6px;justify-content:flex-end}
.finder{position:absolute;left:262px;top:318px;width:398px;height:62px;background:var(--navy);padding:8px 10px;display:grid;grid-template-columns:150px 150px 30px;gap:6px 10px}
.finder span{background:var(--white);height:18px;font-size:8px;color:#999;padding:4px 6px}
.finder .go{grid-column:3;grid-row:2;background:var(--green);display:flex;align-items:center;justify-content:center;padding:0}
.strip{position:absolute;left:22px;top:386px;width:637px;height:14px;background:var(--green)}
.record{position:absolute;left:22px;top:400px;width:637px;height:408px;background:radial-gradient(ellipse at 68% 55%,#6b6b6b,#2d2d2d 60%,#1b1b1b)}
.record-panel{position:absolute;left:8px;top:10px;width:310px;height:398px;background:var(--grey-panel);color:var(--white);padding:10px 14px}
.record-panel h2{font-size:15px;font-weight:700;margin-bottom:10px}
.record-panel dl{font-size:9.5px;line-height:13.4px;padding-left:16px}
.record-panel div{display:flex;gap:3px}
.features{position:absolute;left:22px;top:820px;width:637px;display:flex;gap:22px;justify-content:space-between}
.feature{width:197px;height:178px;background:var(--white)}
.feature h3{background:var(--green);color:var(--white);font-weight:400;font-size:16px;text-align:center;padding:4px 0}
.feature-body{display:flex;gap:8px;padding:10px}
.feature-thumb{width:75px;height:90px;background:var(--navy)}
.feature-body p{font-size:7.5px;line-height:1.45;color:var(--muted);flex:1}
.feature .btn{display:block;width:70px;margin:2px auto 0;text-align:center;background:var(--navy);font-size:7px}
.footer{position:absolute;left:22px;top:1030px;width:637px;display:grid;grid-template-columns:repeat(4,1fr);color:var(--white)}
.footer h4{font-weight:400;font-size:11px;padding-bottom:6px;border-bottom:1px solid rgba(255,255,255,.35);margin-bottom:6px;width:130px}
.footer li{list-style:none;font-size:8px;line-height:14px;color:#cfe0f0}
.bottom-bar{position:absolute;left:22px;top:1160px;width:637px;height:24px;border-top:1px solid rgba(255,255,255,.25);display:flex;align-items:center;justify-content:center;gap:0}
.bottom-bar a{color:var(--white);font-size:7px;padding:0 14px;text-decoration:none;border-left:1px solid rgba(255,255,255,.5)}
.bottom-bar a:first-child{border-left:0}
.social{position:absolute;right:0;top:0;display:flex;gap:6px}
.social i{width:14px;height:14px;border-radius:50%;background:var(--green);display:block}
</style>
</head>
<body>
<div class="page">
  <header class="header">
    <div class="logo">PLINKOR</div>
    <div class="header-actions">
      <a class="btn" href="#">Login</a>
      <a class="btn btn-dark" href="#">Sign up</a>
      <span class="search-input">search</span>
      <span class="search-btn"><svg width="11" height="11" viewBox="0 0 12 12"><circle cx="5" cy="5" r="3.5" fill="none" stroke="#fff" stroke-width="1.6"/><line x1="7.6" y1="7.6" x2="11" y2="11" stroke="#fff" stroke-width="1.6"/></svg></span>
    </div>
  </header>
  <nav class="nav"><a href="#">HOME</a><a href="#">SEARCH BY NUMBER</a><a href="#">VIN LOOKUP</a><a href="#">COMPLETE LIST</a><a href="#">CONTACT US</a></nav>

  <section class="hero">
    <div class="hero-photo" role="img" aria-label="Silver sedan, side view"></div>
    <div class="hero-copy">
      <h1>Rescue Training<br>Programs &amp; Courses</h1>
      <p>Lorem ipsum dolor sit amet consectetur elit ipsum dolor sit amet consectetur adipiscing elit.</p>
      <div class="actions"><a class="btn btn-dark" href="#">Learn More</a><a class="btn btn-dark" href="#">Buy Now</a></div>
    </div>
  </section>
  <form class="finder">
    <span>City, State</span><span>Type of vehicle</span><span style="visibility:hidden"></span>
    <span>enter VIN</span><span>Key Words</span>
    <span class="go"><svg width="11" height="11" viewBox="0 0 12 12"><circle cx="5" cy="5" r="3.5" fill="none" stroke="#fff" stroke-width="1.6"/><line x1="7.6" y1="7.6" x2="11" y2="11" stroke="#fff" stroke-width="1.6"/></svg></span>
  </form>
  <div class="strip"></div>

  <section class="record" role="img" aria-label="Dark sedan, front three-quarter view">
    <div class="record-panel">
      <h2>Customer Name: MARA DULEK</h2>
      <dl>
        <div><dt>Address:</dt><dd>2208 AMBER FIELD LN</dd></div>
        <div><dt>City:</dt><dd>HARLOW BAY</dd></div>
        <div><dt>State:</dt><dd>ST</dd></div>
        <div><dt>Zip:</dt><dd>20418</dd></div>
        <div><dt>Year:</dt><dd>2007</dd></div>
        <div><dt>Make:</dt><dd>BREVIK</dd></div>
        <div><dt>Model:</dt><dd>SOLANO</dd></div>
        <div><dt>VIN:</dt><dd>4B7SK42C18D604182</dd></div>
        <div><dt>Trim level:</dt><dd>XLS</dd></div>
        <div><dt>Engine:</dt><dd>3.5L V6 DOHC 24V</dd></div>
        <div><dt>Style:</dt><dd>SEDAN 4-DR</dd></div>
        <div><dt>Made in:</dt><dd>UNITED STATES</dd></div>
        <div><dt>Steering:</dt><dd>Rack &amp; Pinion</dd></div>
        <div><dt>Anti-brake system:</dt><dd>4-Wheel ABS</dd></div>
        <div><dt>Tank size:</dt><dd>18.50 gallon</dd></div>
        <div><dt>Overall Height:</dt><dd>58.50 in</dd></div>
        <div><dt>Overall Length:</dt><dd>197.20 in</dd></div>
        <div><dt>Overall Width:</dt><dd>72.80 in</dd></div>
        <div><dt>Standard Seating:</dt><dd>5</dd></div>
        <div><dt>Optional Seating:</dt><dd>No data</dd></div>
        <div><dt>Highway Mileage:</dt><dd>31 miles/gallon</dd></div>
        <div><dt>City Mileage:</dt><dd>22 miles/gallon</dd></div>
        <div><dt>Transmission:</dt><dd>5-speed Automatic</dd></div>
      </dl>
    </div>
  </section>

  <section class="features">
    <article class="feature"><h3>Vehicles</h3>
      <div class="feature-body"><div class="feature-thumb" role="img" aria-label="Vehicles photo"></div><p>Lorem ipsum dolor sit amet consectetur adipiscing elit sed lorem ipsum dolor sit amet adipiscing elit sed do eiusmod tempor.</p></div>
      <a class="btn" href="#">VIEW DETAILS</a></article>
    <article class="feature"><h3>About us</h3>
      <div class="feature-body"><div class="feature-thumb" role="img" aria-label="About us photo"></div><p>Lorem ipsum dolor sit amet consectetur adipiscing elit sed lorem ipsum dolor sit amet adipiscing elit sed do eiusmod tempor.</p></div>
      <a class="btn" href="#">VIEW DETAILS</a></article>
    <article class="feature"><h3>Statistics</h3>
      <div class="feature-body"><div class="feature-thumb" role="img" aria-label="Statistics photo"></div><p>Lorem ipsum dolor sit amet consectetur adipiscing elit sed lorem ipsum dolor sit amet adipiscing elit sed do eiusmod tempor.</p></div>
      <a class="btn" href="#">VIEW DETAILS</a></article>
  </section>

  <footer class="footer">
    <div><h4>About Us</h4><ul><li>General Information</li><li>Our Mission</li></ul></div>
    <div><h4>Customer Reviews</h4><ul><li>Adipiscing Elit</li><li>Ipsum Lorem Sit Amet</li></ul></div>
    <div><h4>Support Materials</h4><ul><li>Lorem Ipsum</li><li>Dolor Sit Amet Consectetur</li></ul></div>
    <div><h4>Contact Us</h4><ul><li>Social Page</li><li>News Feed</li><li>Email us</li></ul></div>
  </footer>
  <div class="bottom-bar">
    <a href="#">HOME</a><a href="#">ABOUT</a><a href="#">REVIEWS</a><a href="#">CONTACT</a>
    <div class="social" style="top:5px"><i></i><i></i><i></i></div>
  </div>
</div>
</body>
</html>
```